Granite Ridge Response Business Card

Side 1: Granite Ridge Response Logo (logo without Maltese cross) with industrial rope rescue related theme. Our company services - TRAINING - Fire Training, Confined Space Rescue Training, Rope Rescue training, Hazmat Training, Incident Command, EMS, Pump Operations Training. Website - graniteridgeresponse.example.
Side 2: Granite Ridge Response Fire Department Logo (logo with Maltese cross) with Firefighter related theme. Company (division) services - FIELD SERVICES - Fire Department, Stand-by Rescue, Safety, EMS, Planning. "Supporting the Emergency Response Community Since 1967"

Add contact information wherever it makes since (Name, Email, Phone).
I would like it to represent the Granite Ridge Response Fire Department Logo as a division not as a separate entity without saying it, possibly by depicting it in the background of Side 2 instead of being a standalone picture like the logo on Side 1.

```html
<!DOCTYPE html>
<html lang="en">
<head>
<meta charset="utf-8">
<title>Granite Ridge Response – Business Card</title>
<link href="https://fonts.googleapis.com/css2?family=Lato:wght@400;700;900&family=Montserrat:wght@700;800;900&family=Oswald:wght@700&display=swap" rel="stylesheet">
<style>
  :root{
    --stage:#e4e4e4;
    --ink:#1c1c1c;
    --paper:#ffffff;
    --red:#e8202a;
    --red-soft:#e9483a;
    --bright-red:#f21b1b;
    --white:#ffffff;
  }
  *{margin:0;padding:0;box-sizing:border-box}
  html,body{width:1200px;height:924px;overflow:hidden;background:var(--stage)}
  .canvas{position:relative;width:1200px;height:924px}
  .card{position:absolute;width:620px;height:354px;border-radius:4px;overflow:hidden;box-shadow:0 6px 18px rgba(0,0,0,.18)}

  /* Side 1 – training */
  .card-training{left:60px;top:60px;background:var(--ink);color:var(--white);text-align:center}
  .brand{display:flex;align-items:center;justify-content:center;gap:14px;margin-top:58px}
  .brand-mark{width:26px;height:26px;background:var(--red)}
  .brand-name{font-family:"Montserrat",sans-serif;font-weight:900;font-size:34px;letter-spacing:1px;text-transform:uppercase;color:var(--red)}
  .section-rule{display:flex;align-items:center;justify-content:center;gap:16px;margin-top:30px}
  .section-rule::before,.section-rule::after{content:"";height:3px;width:110px;background:var(--red)}
  .section-title{font-family:"Montserrat",sans-serif;font-weight:800;font-size:24px;color:var(--red);letter-spacing:.5px}
  .services{font-family:"Lato",sans-serif;font-size:15px;line-height:1.6;margin-top:22px}
  .website{font-family:"Montserrat",sans-serif;font-weight:700;font-size:15px;letter-spacing:4px;color:var(--red);margin-top:20px}

  /* Side 2 – field services */
  .card-field{left:520px;top:510px;background:var(--paper)}
  .band{position:absolute;right:0;top:0;width:190px;height:100%;background:var(--bright-red);clip-path:polygon(60% 0,100% 0,100% 100%,0 100%,0 60%)}
  .division-mark{position:absolute;left:318px;top:28px;width:270px;height:270px;border-radius:50%;border:10px solid var(--white);background:var(--white);box-shadow:0 0 0 6px var(--red-soft) inset;display:flex;align-items:center;justify-content:center;text-align:center;padding:30px}
  .division-name{font-family:"Lato",sans-serif;font-weight:900;font-size:26px;line-height:1.15;color:var(--red-soft);text-transform:uppercase}
  .details{position:absolute;left:34px;top:34px;width:300px}
  .person-name{font-family:"Oswald",sans-serif;font-weight:700;font-size:34px;color:var(--red);text-transform:uppercase;letter-spacing:.5px;line-height:1}
  .contact{list-style:none;margin-top:12px;font-family:"Lato",sans-serif;font-size:14px;color:var(--ink)}
  .contact li{display:flex;align-items:center;gap:9px;margin:4px 0;white-space:nowrap}
  .contact svg{width:13px;height:13px;flex:none;fill:var(--red)}
  .field-title{font-family:"Montserrat",sans-serif;font-weight:800;font-size:21px;color:var(--red);margin-top:16px}
  .field-list{list-style:none;margin-top:6px;font-family:"Lato",sans-serif;font-size:15px;color:var(--ink)}
  .field-list li{display:flex;align-items:center;gap:10px;margin:4px 0}
  .tick{width:16px;height:16px;flex:none}
  .tagline{font-family:"Lato",sans-serif;font-weight:900;font-size:14px;line-height:1.3;color:var(--red);margin-top:14px}
</style>
</head>
<body>
<main class="canvas">

  <section class="card card-training">
    <div class="brand">
      <span class="brand-mark"></span>
      <span class="brand-name">Granite Ridge Response</span>
    </div>
    <div class="section-rule"><h2 class="section-title">OUR TRAINING</h2></div>
    <p class="services">Fire Training | Confined Space Rescue Training | Rope Rescue Training<br>Hazmat Training | Incident Command | EMS | Pump Operations Training</p>
    <p class="website">WWW.GRANITERIDGERESPONSE.EXAMPLE</p>
  </section>

  <section class="card card-field">
    <div class="band"></div>
    <div class="division-mark"><span class="division-name">Granite Ridge Response</span></div>

    <div class="details">
      <h1 class="person-name">Daniel Reyes</h1>
      <ul class="contact">
        <li><svg viewBox="0 0 24 24"><path d="M6.6 10.8a15 15 0 0 0 6.6 6.6l2.2-2.2a1 1 0 0 1 1-.25 11.4 11.4 0 0 0 3.6.57 1 1 0 0 1 1 1V20a1 1 0 0 1-1 1A17 17 0 0 1 3 4a1 1 0 0 1 1-1h3.5a1 1 0 0 1 1 1c0 1.25.2 2.45.57 3.57a1 1 0 0 1-.25 1z"/></svg>(555) 014-2290</li>
        <li><svg viewBox="0 0 24 24"><path d="M2 5h20v14H2z M2 5l10 8 10-8" stroke="#fff" stroke-width="1.5"/></svg>dreyes@graniteridgeresponse.example</li>
        <li><svg viewBox="0 0 24 24"><circle cx="12" cy="12" r="10"/><path d="M2 12h20M12 2c3 3 3 17 0 20M12 2c-3 3-3 17 0 20" stroke="#fff" stroke-width="1.4" fill="none"/></svg>graniteridgeresponse.example</li>
      </ul>
      <h2 class="field-title">FIELD SERVICES</h2>
      <ul class="field-list">
        <li><svg class="tick" viewBox="0 0 16 16"><circle cx="8" cy="8" r="8" fill="#e8202a"/><path d="M4.5 8.2l2.3 2.3 4.7-4.7" stroke="#fff" stroke-width="2" fill="none"/></svg>Fire Department</li>
        <li><svg class="tick" viewBox="0 0 16 16"><circle cx="8" cy="8" r="8" fill="#e8202a"/><path d="M4.5 8.2l2.3 2.3 4.7-4.7" stroke="#fff" stroke-width="2" fill="none"/></svg>Stand-by Rescue</li>
        <li><svg class="tick" viewBox="0 0 16 16"><circle cx="8" cy="8" r="8" fill="#e8202a"/><path d="M4.5 8.2l2.3 2.3 4.7-4.7" stroke="#fff" stroke-width="2" fill="none"/></svg>Safety | EMS | Planning</li>
      </ul>
      <p class="tagline">Supporting the Emergency<br>Response Community Since 1967</p>
    </div>
  </section>

</main>
</body>
</html>
```